The company Velquist needs a design for CBD capsules

We (Velquist) need a new design for our CBD capsules. We already have a design for CBD oil. However, we do not want to use this completely. The Talmbex label and the cans serve as a template. Please upload in the format 139mm x 59mm incl.
2mm bleed all around and in .pdf vector. The logo files for Velquist are included in the briefing.

Industry/Entity Type

Onlineshop

Colors
00AB8E
00BBA5
67D7C9
C6EFE9
E9F9F6

Requirements
Must have
• Please in the format 139mm x 59mm incl. 2mm bleed all around and .pdf vector
Should not have
• It shouldn't be the same label, but it should be recognizable.

```html
<!DOCTYPE html>
<html lang="de">
<head>
<meta charset="utf-8">
<title>Velquist CBD Capsules – Verpackung</title>
<link rel="stylesheet" href="https://fonts.googleapis.com/css2?family=Oswald:wght@300;400;600&family=Roboto:wght@700;900&family=Allura&display=swap">
<style>
  :root {
    --backdrop: #afc4a5;
    --teal-dark: #1f4b5a;
    --teal-mid: #2a5f6f;
    --teal-light: #4a8290;
    --side-dark: #173c49;
    --white: #ffffff;
    --paper: #f1f2f2;
    --ink: #1f4b5a;
    --side-text: #d5e2e6;
    --leaf: #3f7a3a;
    --leaf-dark: #1f3f22;
  }
  * { margin: 0; padding: 0; box-sizing: border-box; }
  html, body { width: 1200px; height: 1056px; overflow: hidden; }
  body { background: var(--backdrop); position: relative; font-family: "Oswald", sans-serif; }

  .packaging { position: absolute; left: 130px; top: 218px; display: flex; }

  .side-panel {
    width: 320px; height: 620px;
    background: linear-gradient(180deg, var(--teal-mid), var(--side-dark));
    color: var(--side-text);
    padding: 60px 28px 0 30px;
    font-weight: 300; font-size: 11.5px; line-height: 1.45;
  }
  .side-panel p { margin-bottom: 13px; }
  .side-panel strong { font-weight: 600; }
  .side-panel .product-title { font-weight: 600; text-transform: uppercase; }
  .side-panel .net-content { padding-bottom: 14px; border-bottom: 1px solid var(--side-text); }

  .front-panel {
    position: relative; width: 620px; height: 620px; overflow: hidden;
    background: linear-gradient(200deg, var(--teal-light) 0%, var(--teal-mid) 45%, var(--teal-dark) 100%);
  }
  .label-base { position: absolute; left: 0; top: 0; }

  .brand-name {
    position: absolute; top: 60px; left: 0; width: 640px; text-align: center;
    font-family: "Roboto", sans-serif; font-weight: 700; font-size: 52px; line-height: 1; color: var(--white);
    display: flex; justify-content: center; align-items: center; gap: 12px;
  }
  .brand-dot { width: 14px; height: 14px; border-radius: 50%; background: var(--white); }
  .product-name {
    position: absolute; top: 160px; left: 0; width: 640px; text-align: center;
    font-family: "Roboto", sans-serif; font-weight: 900; font-size: 150px; line-height: 1; color: var(--white);
  }
  .product-type {
    position: absolute; top: 312px; left: 0; width: 640px; text-align: center;
    font-family: "Roboto", sans-serif; font-weight: 700; font-size: 34px; line-height: 1; letter-spacing: 7px; color: var(--white);
  }
  .illustration {
    position: absolute; left: 458px; top: 290px; width: 150px; height: 180px;
    border-radius: 45% 50% 40% 45%;
    background: radial-gradient(ellipse at 50% 55%, var(--leaf-dark) 0%, var(--leaf) 55%, rgba(63,122,58,0.25) 100%);
  }
  .claims {
    position: absolute; left: 150px; top: 432px; list-style: none;
    color: var(--ink); font-size: 22px; line-height: 1.45;
  }
  .claims li { display: flex; align-items: center; gap: 8px; }
  .strength {
    position: absolute; left: 478px; top: 500px; color: var(--white);
    font-family: "Oswald", sans-serif; font-weight: 600; font-size: 34px; line-height: 1;
  }
  .spectrum {
    position: absolute; left: 90px; top: 522px; color: var(--ink);
    font-family: "Allura", cursive; font-size: 58px; line-height: 1;
  }
</style>
</head>
<body>
  <main class="packaging">
    <section class="side-panel">
      <p class="product-title">Nahrungsergänzungsmittel mit Vollspektrum-Hanf-Extrakt in Bio-Hanfsamenöl</p>
      <p><strong>Inhalt:</strong> CBD Wert: 10% (+/- 482mg) THC Wert: &lt; 0,04% Träger der Wirkstoffe ist BIO Hanföl, Kapseln aus 114 mg Gelatine und 57 mg Glycerol</p>
      <p><strong>Verzehrmenge:</strong> Erwachsene 1x1 Softgel-Kapsel unzerkaut mit ausreichend Flüssigkeit</p>
      <p>Die angegebene empfohlene Verzehrmenge darf nicht überschritten werden. Nahrungsergänzungsmittel sind kein Ersatz für eine ausgewogene und abwechslungsreiche Ernährung</p>
      <p><strong>Hinweis:</strong> Kühl (max.25 °C) trocken und vor Licht geschützt lagern. Außerhalb von Reichweite kleiner Kinder aufbewahren</p>
      <p><strong>Mindestens haltbar bis Ende:</strong> siehe Boden<br><strong>LOS-Nr.:</strong> siehe Boden</p>
      <p class="net-content">60 Kapseln e 39g</p>
    </section>

    <section class="front-panel">
      <svg class="label-base" width="620" height="620" viewBox="0 0 620 620" aria-hidden="true">
        <path d="M0 480 C 140 400 330 350 620 340 L620 620 L0 620 Z" fill="var(--paper)"/>
        <circle cx="570" cy="610" r="170" fill="var(--teal-mid)"/>
      </svg>

      <div class="brand-name"><span>Velquist</span><span class="brand-dot"></span></div>
      <div class="product-name">CBD</div>
      <div class="product-type">CAPSULES</div>

      <div class="illustration" role="img" aria-label="Hanfblatt mit dunklen Softgel-Kapseln"></div>

      <ul class="claims">
        <li><svg width="22" height="20" viewBox="0 0 22 20" aria-hidden="true"><path d="M2 11 L8 17 L20 3" fill="none" stroke="var(--ink)" stroke-width="3.5"/></svg>VEGAN</li>
        <li><svg width="22" height="20" viewBox="0 0 22 20" aria-hidden="true"><path d="M2 11 L8 17 L20 3" fill="none" stroke="var(--ink)" stroke-width="3.5"/></svg>GENTECHNIK FREI</li>
      </ul>

      <div class="strength">10%</div>
      <div class="spectrum">Vollspektrum</div>
    </section>
  </main>
</body>
</html>
```